Organic Herbs & Spices container

Greek startup company, which cultivate and trade spices and herbs (such as oregano, mint, thyme, sage etc.)

At present we are interested in only the type and shape of packaging which should be made by materials such as paper, cardboard, laminated paper and others based on paper or plastic.

Package size vary from 80g (2.82oz) - 300g (10.58oz). We are going to use the same packing for a variety of products with different information

* Please find attached our logo which should be included in the design.
* There is no company name available at the moment, however a name placeholder should be included.
* include a placeholder for the type of product (sage, oregano, mint, tea etc...).
* Each package should have a place in order to include product details and nutrition facts.

e.g.
xxxx (company name placeholder)
Sage (product type)
product details and nutrition facts.
Updates

Dear designers,first of all, thank you for your proposals. Please find bellow some updates for the project.- It is mandatory to include the logo into the design - Each package should be able to stored vertically - We are looking for one specific package design, please do not submit many variations of a certain package neither colour differentiations Thanks and good luck Added Wednesday, September 28, 2016

Please avoid the use of images. The same package will be used for all the kinds of products (only name and maybe colour will be different among different products. A transparent frame that will show the contents could be used too) Added Wednesday, September 28, 2016

Please find attached logo in EPS format

Our logo is the baseline, any concepts should be based on it. Try to avoid just adding the logo as a small sticker somewhere on the design. Please try to create around it at any way toy like. This could be, to visualize it as a 3D shape or object which can be used as the container of the products.

Reason: We would like to extend the time of the project. We believe that most of the submitted designs do not comply with our requirements.

Reason: We would like to see a bigger variety of ideas

Target Market(s)

Pretty much to anyone over 20 years old worldwide.

Industry/Entity Type

Nutrition

Requirements
Must have
• It should be attractive, easily recognized, simple yet innovative, durable, functional (easy to use) and easy to store.
Should not have
• Project must not include complex or obnoxious shapes and colours.

```html
<!DOCTYPE html>
<html lang="en">
<head>
<meta charset="utf-8">
<title>Thymelia Herbs &amp; Spices – Packaging Concept</title>
<link rel="stylesheet" href="https://fonts.googleapis.com/css2?family=Tinos:wght@700&family=Open+Sans:wght@400&display=swap">
<style>
  :root {
    --page: #ffffff;
    --kraft: #c7ae88;
    --ink: #1f1a14;
    --herb-dark: #3e5a2c;
    --herb-light: #7d9a5e;
    --line: #1a1a1a;
    --card-brown: #9a6a24;
    --label-tint: #e6e6e6;
    --shadow: rgba(0, 0, 0, 0.35);
  }
  * { margin: 0; padding: 0; box-sizing: border-box; }
  html, body { width: 848px; height: 1200px; overflow: hidden; background: var(--page); }
  .sheet { position: relative; width: 848px; height: 1200px; }

  .serif { font-family: "Tinos", "Times New Roman", serif; font-weight: 700; color: var(--ink); }

  .panel {
    position: absolute; top: 70px; width: 288px; height: 600px;
    background: var(--kraft);
    box-shadow: 3px 4px 6px var(--shadow);
  }
  .panel--front { left: 82px; }
  .panel--back { left: 462px; }

  .brand { position: absolute; left: 0; right: 0; text-align: center; }
  .brand__name { top: 18px; font-size: 44px; letter-spacing: 0.5px; line-height: 1; }
  .brand__line { top: 60px; font-size: 23px; line-height: 1; }

  .window {
    position: absolute; left: 30px; top: 232px; width: 228px; height: 284px;
    border-radius: 16px;
    background: radial-gradient(ellipse at 45% 45%, var(--herb-light), var(--herb-dark));
  }

  .product-name { position: absolute; left: 23px; top: 550px; font-size: 37px; line-height: 1; }
  .net-weight { position: absolute; left: 220px; top: 560px; font-size: 20px; line-height: 1; }

  .nutrition { position: absolute; left: 0; right: 0; top: 138px; text-align: center; }
  .nutrition__title { font-size: 18px; line-height: 1; margin-bottom: 10px; }
  .nutrition__group { font-size: 20px; line-height: 24.5px; margin-bottom: 24px; }

  .bag {
    position: absolute; left: 136px; top: 730px; width: 181px; height: 423px;
    border: 2px solid var(--line); background: var(--page);
  }
  .bag__seal { position: absolute; left: 0; right: 0; top: 33px; border-top: 2px solid var(--line); }
  .bag__label { position: absolute; left: 0; right: 0; top: 90px; height: 230px; }
  .bag__disc {
    position: absolute; left: 34px; top: 50px; width: 110px; height: 110px;
    border-radius: 50%; background: var(--label-tint);
  }
  .bag__text { position: absolute; left: 0; right: 0; text-align: center; }
  .bag__brand { top: 84px; font-size: 18px; line-height: 1; }
  .bag__sub { top: 102px; font-size: 11px; line-height: 1; }
  .bag__product { top: 115px; font-size: 22px; line-height: 1; }

  .note {
    position: absolute; font-family: "Open Sans", Arial, sans-serif; font-weight: 400;
    font-size: 23px; line-height: 32px; color: var(--line);
  }
  .note--bag { left: 328px; top: 742px; }
  .note--holder { left: 428px; top: 966px; }

  .holder { position: absolute; left: 620px; top: 705px; width: 180px; height: 445px; }
</style>
</head>
<body>
<main class="sheet">

  <section class="panel panel--front" aria-label="Front of box">
    <h1 class="brand brand__name serif">THYMELIA</h1>
    <p class="brand brand__line serif">Herbs &amp; Spices</p>
    <div class="window" role="img" aria-label="Clear window showing the dried sage leaves inside"></div>
    <p class="product-name serif">SAGE</p>
    <p class="net-weight serif">300g</p>
  </section>

  <section class="panel panel--back" aria-label="Back of box">
    <h2 class="brand brand__name serif">THYMELIA</h2>
    <p class="brand brand__line serif">Herbs &amp; Spices</p>
    <div class="nutrition serif">
      <h3 class="nutrition__title">NUTRITION FACTS</h3>
      <p class="nutrition__group">omomomomomomo<br>omomomomomomo<br>omomomomomomo<br>omomomomomomo</p>
      <p class="nutrition__group">omomomomomomo<br>omomomomomomo<br>omomomomomomo<br>omomomomomomo</p>
      <p class="nutrition__group">omomomomomomo<br>omomomomomomo<br>omomomomomomo<br>omomomomomomo</p>
      <p class="nutrition__group">omomomomomomo<br>omomomomomomo</p>
    </div>
  </section>

  <div class="bag" aria-label="Resealable clear bag">
    <div class="bag__seal"></div>
    <div class="bag__label">
      <div class="bag__disc"></div>
      <p class="bag__text bag__brand serif">THYMELIA</p>
      <p class="bag__text bag__sub serif">Herbs &amp; Spices</p>
      <p class="bag__text bag__product serif">SAGE</p>
    </div>
  </div>
  <p class="note note--bag">Resealable<br>clear bag with<br>one colour paper<br>label on the bag</p>

  <svg class="holder" viewBox="0 0 180 445" aria-label="Cardboard triangle holder">
    <polygon points="81,7 94,7 168,435 8,435" fill="none" stroke="var(--card-brown)" stroke-width="4"/>
    <polygon points="88,17 157,425 19,425" fill="none" stroke="var(--line)" stroke-width="1.5"/>
  </svg>
  <p class="note note--holder">Cardboard triangle<br>holds the herbs in<br>a resealable<br>clear bag</p>

</main>
</body>
</html>
```